Marlow Ridgeway a PlateWork Fabricator! Pressure Vessels, Stainless Vessels, Steel Fabricator!

Update and modernize the www.marlowridgeway.example website. Basically throwing away the old site and coming back with a new feel, new look, but some of the same content. One of our other companies is www.keltonbuilders.example and if you view that site you will get a idea of how we would like the site to feel. Below are the MR logos and the colors are #231F20 and #6D0B17 and the font is Ethnocentric Rg.

Target Market(s)

Steel Fabrication, Platework, Vessel Fabrication,

Industry/Entity Type

Steel

Coding

Coded - Design and coding required

Number of Pages Required

5+ page

Font styles to use
Other font styles liked:
• Ethnocentric Rg

Requirements
Must have
• Industry feel... site must flow and color scheme and font be consistent.

```html
<!DOCTYPE html>
<html lang="en">
<head>
<meta charset="utf-8">
<title>Marlow Ridgeway — Fabrication Services</title>
<link rel="stylesheet" href="https://fonts.googleapis.com/css2?family=Orbitron:wght@700;800;900&family=Roboto:wght@400;500;700&family=Oswald:wght@500&display=swap">
<style>
:root{
  --ink:#231F20;
  --ink-deep:#1b1819;
  --ink-soft:#2c2829;
  --brand:#6D0B17;
  --brand-bright:#8a0f1d;
  --white:#ffffff;
  --text:#e4e1e1;
  --muted:#8f8a8b;
  --line:#5a5556;
}
*{box-sizing:border-box;margin:0;padding:0}
html,body{width:1200px;height:3468px;overflow:hidden;background:var(--ink)}
body{position:relative;font-family:"Roboto",Arial,sans-serif;color:var(--text)}
.abs{position:absolute}
.display{font-family:"Orbitron",Arial,sans-serif;font-weight:900;color:var(--white);text-transform:uppercase;letter-spacing:3px}
.btn{position:absolute;display:flex;align-items:center;justify-content:center;font-family:"Roboto",Arial,sans-serif;font-weight:700;font-size:13px;text-transform:uppercase;color:var(--white);background:var(--brand);letter-spacing:.3px}
.btn--ghost{background:transparent;border:2px solid var(--white)}

/* header */
.site-header{position:absolute;left:0;top:0;width:1200px;height:102px;background:var(--ink-deep)}
.brand{position:absolute;left:88px;top:36px;display:flex;align-items:center;gap:10px;font-family:"Roboto",Arial,sans-serif;font-weight:700;font-size:20px;color:var(--white);text-transform:uppercase}
.brand-dot{width:30px;height:30px;border:3px solid var(--white);border-radius:50%}
.main-nav{position:absolute;left:335px;top:48px;display:flex;gap:36px;font-size:14px;font-weight:500;color:var(--white)}
.main-nav .active{color:var(--brand-bright)}

/* hero */
.hero-photo{left:451px;top:102px;width:749px;height:499px;background:radial-gradient(circle at 60% 40%,#5b4a3c 0%,#2b2523 45%,#141112 100%)}
.hero-kicker{left:90px;top:288px;font-size:27px;font-weight:500;color:var(--white)}
.hero-title{left:88px;top:322px;font-size:52px;line-height:52px;letter-spacing:4px}

/* quality */
.pipes{left:0;top:660px;width:497px;height:430px;background:linear-gradient(135deg,#6d6b6c 0%,#2e2b2c 55%,#1a1718 100%)}
.quality-title{left:576px;top:760px;font-size:26px;line-height:33px}
.copy{font-size:15px;line-height:25px;color:var(--text)}

/* success band */
.metal{left:0;width:1200px;background:linear-gradient(180deg,#2a2627 0%,#3a3536 45%,#262223 100%)}
.rivet{width:30px;height:30px;border-radius:50%;background:radial-gradient(circle at 40% 35%,#9c9798 0%,#4a4546 60%,#2a2627 100%)}
.success-title{left:88px;top:1325px;font-size:26px}
.weld-photo{left:694px;top:1235px;width:416px;height:416px;border-radius:50%;background:radial-gradient(circle at 50% 40%,#9a6a3a 0%,#5b4a40 35%,#2f2a2a 80%)}
.badge{left:689px;top:1506px;width:110px;height:110px;border-radius:50%;background:var(--ink);border:6px solid var(--white);display:flex;align-items:center;justify-content:center;font-family:"Orbitron",Arial,sans-serif;font-weight:800;font-size:34px;color:var(--white)}

/* testimonial */
.testimonial{left:0;top:1741px;width:1200px;height:717px;background:linear-gradient(180deg,#231F20 0%,#231F20 45%,#5c5858 78%,#1e1b1c 100%)}
.field-scene{left:0;top:2090px;width:1200px;height:368px;background:linear-gradient(180deg,rgba(35,31,32,0) 0%,rgba(90,86,86,.35) 45%,rgba(20,18,19,.9) 100%)}
.quote-mark{left:88px;top:1956px;font-family:"Oswald",sans-serif;font-size:56px;line-height:56px;color:var(--brand-bright)}
.quote-kicker{left:134px;top:1975px;font-family:"Oswald",sans-serif;font-weight:500;font-size:22px;color:var(--white);text-transform:uppercase}
.quote-title{left:134px;top:2003px;font-size:25px;line-height:30px}

/* quote form */
.form-title{left:0;width:1200px;top:2612px;text-align:center;font-size:26px}
.field{position:absolute;border-bottom:1px solid var(--line);font-size:14px;font-weight:500;color:var(--white);padding-left:20px}

/* footer */
.site-footer{left:0;top:3105px;width:1200px;height:363px;background:var(--ink)}
.footer-brand{left:88px;top:3240px;display:flex;align-items:center;gap:14px;font-family:"Roboto",Arial,sans-serif;font-weight:700;font-size:30px;line-height:30px;color:var(--white);text-transform:uppercase}
.footer-brand .ring{width:66px;height:66px;border:5px solid var(--white);border-radius:50%}
.footer-head{font-size:17px;letter-spacing:3px}
.contact-line{font-size:16px;font-weight:500;color:var(--white);display:flex;align-items:center;gap:10px}
.social{width:36px;height:36px;border-radius:50%;background:#2f6fb8}
.rule{left:88px;top:3410px;width:1024px;height:1px;background:#3a3536}
.legal{left:0;width:1200px;top:3432px;text-align:center;font-size:12px;font-weight:700;color:var(--white);text-transform:uppercase}
.to-top{left:1128px;top:3394px;width:32px;height:32px;background:var(--brand);display:flex;align-items:center;justify-content:center}
</style>
</head>
<body>

<header class="site-header">
  <div class="brand"><span class="brand-dot"></span>Marlow Ridgeway</div>
  <nav class="main-nav">
    <span class="active">Home</span><span>About</span><span>Products</span><span>Services</span><span>Who we serve</span><span>Resources</span><span>Contact</span>
  </nav>
  <a class="btn" style="left:966px;top:42px;width:146px;height:34px;font-size:11px">Request a quote</a>
</header>

<section>
  <div class="abs hero-photo" role="img" aria-label="Welder in a helmet cutting steel with sparks flying"></div>
  <p class="abs hero-kicker">Your vision, Our custom quality</p>
  <h1 class="abs display hero-title">Fabrication<br>Services</h1>
  <a class="btn" style="left:90px;top:444px;width:157px;height:42px">View product</a>
</section>

<section>
  <div class="abs pipes" role="img" aria-label="Stack of polished steel pipes"></div>
  <h2 class="abs display quality-title">Quality Assurance<br>Guaranteed</h2>
  <p class="abs copy" style="left:578px;top:830px;width:540px">As experienced steel fabricators, we anticipate your needs and requirements from vision to production to delivery. Your steel fabrication products are manufactured by proven business processes and some of the industry's top experts.</p>
  <a class="btn" style="left:578px;top:929px;width:127px;height:40px">Products</a>
  <a class="btn btn--ghost" style="left:714px;top:929px;width:128px;height:40px">Services</a>
</section>

<section>
  <div class="abs metal" style="top:1091px;height:650px"></div>
  <span class="abs rivet" style="left:54px;top:1146px"></span>
  <span class="abs rivet" style="left:1118px;top:1146px"></span>
  <span class="abs rivet" style="left:54px;top:1659px"></span>
  <span class="abs rivet" style="left:1118px;top:1659px"></span>
  <h2 class="abs display success-title">Success at any size</h2>
  <p class="abs copy" style="left:90px;top:1365px;width:560px">We deliver fabrication solutions from small scale projects to our specialized oversized and overweight fabrication, processing, and handling capabilities. Steel fabricators proudly serving the power generation, water treatment, waste treatment, agriculture, chemical, food processing, mining, oil &amp; gas and heavy industry project sectors for nearly 40 years.</p>
  <a class="btn" style="left:90px;top:1514px;width:148px;height:36px">Who we serve</a>
  <div class="abs weld-photo" role="img" aria-label="Worker grinding steel with a shower of sparks"></div>
  <div class="abs badge">MR</div>
</section>

<section>
  <div class="abs testimonial"></div>
  <div class="abs field-scene" role="img" aria-label="Silhouette of an oil pumpjack at dusk"></div>
  <span class="abs quote-mark">&ldquo;</span>
  <p class="abs quote-kicker">We may not be superheroes but</p>
  <h2 class="abs display quote-title">Our customers think<br>we are.</h2>
  <a class="btn" style="left:139px;top:2081px;width:127px;height:37px">Case studie</a>
  <a class="btn btn--ghost" style="left:275px;top:2081px;width:130px;height:37px">Our clients</a>
  <p class="abs copy" style="left:580px;top:1970px;width:540px">We will keep Marlow-Ridgeway steel fabricators on our bidding list for vessels, tanks and stacks. Our catch tank constructed by them was of excellent workmanship and the exterior and interior met all of our expectations. We were impressed with the knowledgeable sales and engineering staff as well as their facilities. They worked well from the calculations for the foundation to the final tank design.</p>
</section>

<section>
  <div class="abs metal" style="top:2458px;height:647px"></div>
  <span class="abs rivet" style="left:54px;top:2512px"></span>
  <span class="abs rivet" style="left:1118px;top:2512px"></span>
  <span class="abs rivet" style="left:54px;top:3028px"></span>
  <span class="abs rivet" style="left:1118px;top:3028px"></span>
  <h2 class="abs display form-title">Request a quote</h2>
  <div class="field" style="left:303px;top:2683px;width:294px;height:34px">First Name*</div>
  <div class="field" style="left:606px;top:2683px;width:291px;height:34px">Last Name*</div>
  <div class="field" style="left:303px;top:2744px;width:294px;height:35px">Company Name*</div>
  <div class="field" style="left:606px;top:2744px;width:291px;height:35px">Phone Number*</div>
  <div class="field" style="left:303px;top:2797px;width:594px;height:35px">Email*</div>
  <div class="field" style="left:303px;top:2848px;width:594px;height:77px">Describe your project*</div>
  <a class="btn" style="left:509px;top:2946px;width:180px;height:40px">Submit your quote</a>
</section>

<footer>
  <div class="abs site-footer"></div>
  <div class="abs footer-brand"><span class="ring"></span><span>Marlow<br>Ridgeway</span></div>
  <h3 class="abs display footer-head" style="left:439px;top:3236px">Contact us</h3>
  <p class="abs contact-line" style="left:439px;top:3268px">
    <svg width="12" height="14" viewBox="0 0 12 14"><path d="M2 1l3 0 1 3-2 1.5c.8 1.8 2 3 3.5 3.5L9 7l3 1v3c0 1-1 2-2 2C5 13 0 8 0 3 0 2 1 1 2 1z" fill="#8a0f1d"/></svg>555.014.2290</p>
  <p class="abs contact-line" style="left:439px;top:3298px">
    <svg width="14" height="11" viewBox="0 0 14 11"><rect x="0" y="0" width="14" height="11" fill="#8a0f1d"/><path d="M0 0l7 6 7-6" stroke="#231F20" stroke-width="1.5" fill="none"/></svg>info@marlowridgeway.example</p>
  <h3 class="abs display footer-head" style="left:719px;top:3236px">Follow us</h3>
  <span class="abs social" style="left:722px;top:3272px"></span>
  <span class="abs social" style="left:766px;top:3272px"></span>
  <span class="abs social" style="left:810px;top:3272px;background:#1f5f98"></span>
  <a class="btn" style="left:950px;top:3246px;width:162px;height:40px">Start today</a>
  <div class="abs rule"></div>
  <p class="abs legal">© 2018 Marlow-Ridgeway. All rights reserved.</p>
  <div class="abs to-top"><svg width="12" height="8" viewBox="0 0 12 8"><path d="M1 7l5-5 5 5" stroke="#fff" stroke-width="2" fill="none"/></svg></div>
</footer>

</body>
</html>
```